Re design my company logo boost my identity

Hello ,

i am asking for redesign and editing my logo to design a stationery for me
please don't ask many question just let your creativity kicks off .

don't change the logo 360 degree just boost it
my main color is Blue Light please be sure this color appear in your design very well
Blue Light = PANTONE 13-4909

Target Market(s)

young mens and girls 14 to 36 year old

Industry/Entity Type

It Company

Requirements
Must have
• my main color is Blue Light please be sure this color appear in your design very well
• Blue Light = PANTONE 13-4909

```html
<!DOCTYPE html>
<html lang="en">
<head>
<meta charset="utf-8">
<title>lumenix stationery</title>
<link href="https://fonts.googleapis.com/css2?family=Quicksand:wght@500&family=Open+Sans:wght@400;600;700&display=swap" rel="stylesheet">
<style>
  :root {
    --blue: #5cc6da;
    --dark: #35373a;
    --orange: #d8820c;
    --paper: #ffffff;
    --ground: #f2f3f4;
    --ink: #444;
  }
  * { box-sizing: border-box; margin: 0; padding: 0; }
  html, body { width: 1200px; height: 937px; overflow: hidden; }
  body { background: var(--ground); font-family: "Open Sans", sans-serif; color: var(--ink); position: relative; }

  .sheet { position: absolute; background: var(--paper); border: 1px solid #e4e6e8; }

  .brand { position: absolute; display: flex; align-items: center; gap: 6px; }
  .brand-name { font-family: "Quicksand", sans-serif; font-weight: 500; color: var(--blue); line-height: 1; letter-spacing: 1px; }
  .brand-dot { border-radius: 50%; background: var(--orange); flex: none; }

  .band { position: absolute; left: 0; right: 0; bottom: 0; display: flex; }
  .band .sq { flex: none; }
  .band .sq.dark { background: var(--dark); }
  .band .sq.orange { background: var(--orange); }
  .band .strip { flex: 1; background: var(--blue); color: #fff; display: flex; align-items: center; padding-left: 14px; letter-spacing: 3px; }

  /* letterhead */
  .letterhead { left: 185px; top: 68px; width: 388px; height: 544px; }
  .letterhead .brand { left: 33px; top: 48px; }
  .letterhead .brand-name { font-size: 30px; }
  .letterhead .brand-dot { width: 9px; height: 9px; }
  .contact-block { position: absolute; right: 18px; top: 22px; text-align: right; font-size: 6.5px; line-height: 1.25; color: #333; }
  .contact-block .label { font-weight: 700; font-size: 8px; letter-spacing: .8px; }
  .letter { position: absolute; left: 36px; top: 137px; width: 300px; font-size: 5.4px; line-height: 1.55; color: #555; }
  .letter p { margin-bottom: 9px; }
  .letter .gap { margin-bottom: 20px; }
  .letter strong { color: #333; }
  .signature { width: 26px; height: 14px; background: #e9e9e9; margin: 4px 0 6px; }
  .letterhead .band { height: 16px; }
  .letterhead .band .sq { width: 15px; }
  .letterhead .band .strip { font-size: 8.5px; }

  /* blank sheet */
  .plain-sheet { left: 636px; top: 40px; width: 458px; height: 576px; }
  .plain-sheet .brand { left: 50%; top: 255px; transform: translateX(-50%); }
  .plain-sheet .brand-name { font-size: 56px; }
  .plain-sheet .brand-dot { width: 14px; height: 14px; }
  .plain-sheet .band { height: 19px; }
  .plain-sheet .band .sq { width: 19px; }
  .plain-sheet .band .strip { font-size: 10px; }

  /* business cards */
  .card { width: 176px; height: 100px; left: 46px; }
  .card-front { top: 658px; }
  .card-back { top: 785px; }
  .card-front .col { position: absolute; top: 12px; font-size: 4.6px; line-height: 1.3; color: #444; }
  .card-front .col .label { font-weight: 700; font-size: 5.6px; letter-spacing: .5px; color: #333; }
  .card-front .col.left { left: 8px; }
  .card-front .col.right { left: 88px; }
  .card-front .brand { left: 8px; top: 58px; }
  .card-front .brand-name { font-size: 13px; }
  .card-front .brand-dot { width: 4px; height: 4px; }
  .person { position: absolute; right: 7px; top: 66px; text-align: right; }
  .person .name { font-weight: 700; font-size: 7px; color: #333; }
  .person .role { font-size: 4.5px; letter-spacing: .6px; margin-top: 4px; }
  .card-front .band { height: 6px; bottom: auto; top: 93px; height: 7px; }
  .card-front .band .sq { width: 6px; }
  .card-back .brand { left: 50%; top: 38px; transform: translateX(-50%); }
  .card-back .brand-name { font-size: 20px; }
  .card-back .brand-dot { width: 6px; height: 6px; }

  /* compliment slip */
  .slip { left: 266px; top: 672px; width: 430px; height: 210px; }
  .slip .brand { left: 36px; top: 34px; }
  .slip .brand-name { font-size: 30px; }
  .slip .brand-dot { width: 9px; height: 9px; }
  .slip .band { height: 14px; bottom: 10px; }
  .slip .band .sq { width: 16px; }
  .slip .band .strip { font-size: 8px; }

  /* envelope back */
  .envelope { left: 737px; top: 672px; width: 432px; height: 207px; overflow: hidden; }
  .envelope .flap { position: absolute; left: 0; top: 0; width: 100%; height: 72px; background: var(--blue); border-radius: 0 0 42px 42px; display: flex; align-items: center; justify-content: center; color: #fff; font-weight: 600; font-size: 14.5px; letter-spacing: 2.5px; }
</style>
</head>
<body>

  <section class="sheet letterhead">
    <div class="brand"><span class="brand-dot"></span><span class="brand-name">lumenix</span></div>
    <div class="contact-block">
      <div class="label">CONTACT US</div>
      <div>014 555 0192</div>
      <div>hello@lumenix.io</div>
      <div>www.lumenix.io</div>
    </div>
    <div class="letter">
      <p>July 2, 2012</p>
      <p><strong>Dear Client,</strong><br>Harbor House, Lane St., Country Name</p>
      <p>We are pleased to share our new stationery with you. Every sheet, card and envelope now carries the same fresh light blue tone, so our studio feels clear and friendly wherever our name appears. Thank you for your steady support over the past years; we look forward to building even more bright ideas together with you and your team.</p>
      <p class="gap">Our updated services list is attached for your review, along with dates for the next planning meeting.</p>
      <p>Please let us know which session suits you best. Our team will prepare short demos of the new tools, bring sample designs, and answer any questions you may have about timing, cost or support. We value every partner and aim to keep each project simple, fast and clear from start to finish.</p>
      <p>Best Regards,</p>
      <div class="signature" role="img" aria-label="Handwritten signature"></div>
      <p><strong>Daniel Reyes</strong><br>Director<br><br>Harbor House, Lane St., Country Name</p>
    </div>
    <div class="band"><span class="sq dark"></span><span class="sq orange"></span><span class="sq dark"></span><span class="sq orange"></span><span class="strip">www.lumenix.io</span></div>
  </section>

  <section class="sheet plain-sheet">
    <div class="brand"><span class="brand-dot"></span><span class="brand-name">lumenix</span></div>
    <div class="band"><span class="sq dark"></span><span class="sq orange"></span><span class="sq dark"></span><span class="sq orange"></span><span class="strip">www.lumenix.io</span></div>
  </section>

  <section class="sheet card card-front">
    <div class="col left">
      <div class="label">CONTACT US</div>
      <div>014 555 0192</div>
      <div>hello@lumenix.io</div>
      <div>www.lumenix.io</div>
    </div>
    <div class="col right">
      <div class="label">FOLLOW US ON SOCIAL</div>
      <div>feed.link/lumenix</div>
      <div>chirp.link/lumenix</div>
      <div>folio.link/lumenix</div>
    </div>
    <div class="brand"><span class="brand-dot"></span><span class="brand-name">lumenix</span></div>
    <div class="person"><div class="name">ALEX MORAN</div><div class="role">FOUNDER</div></div>
    <div class="band"><span class="sq dark"></span><span class="sq orange"></span><span class="sq dark"></span><span class="sq orange"></span><span class="strip"></span></div>
  </section>

  <section class="sheet card card-back">
    <div class="brand"><span class="brand-dot"></span><span class="brand-name">lumenix</span></div>
  </section>

  <section class="sheet slip">
    <div class="brand"><span class="brand-dot"></span><span class="brand-name">lumenix</span></div>
    <div class="band"><span class="sq dark"></span><span class="sq orange"></span><span class="sq dark"></span><span class="sq orange"></span><span class="strip">www.lumenix.io</span></div>
  </section>

  <section class="sheet envelope">
    <div class="flap">www.lumenix.io</div>
  </section>

</body>
</html>
```